New locally owned rental company needs a flyer to circulate

Need flyer with logo, phone# and address. We rent cars to anyone with driver's license and proper insurance. Rates as low as $50/day. Can offer compact cars, mid-size and full size sedans. Also SUV's.

```html
<!DOCTYPE html>
<html lang="en">
<head>
<meta charset="utf-8">
<title>DriveWay Car &amp; Van Rental Flyer</title>
<link href="https://fonts.googleapis.com/css2?family=Antonio:wght@700&family=Red+Hat+Display:ital,wght@0,400;0,800;1,900&display=swap" rel="stylesheet">
<style>
  :root {
    --page: #ffffff;
    --ink: #000000;
    --white: #ffffff;
    --brand-blue: #0a55b4;
    --brand-green: #2fb457;
    --bar-green: #34c66b;
    --tick-yellow: #f3e31b;
    --tag-grey: #7d848e;
    --tag-dark: #141414;
  }
  * { margin: 0; padding: 0; box-sizing: border-box; }
  html, body { width: 1200px; height: 1200px; overflow: hidden; background: var(--page); }
  .flyer {
    position: absolute; left: 202px; top: 86px; width: 804px; height: 1036px;
    background: var(--ink); overflow: hidden;
    box-shadow: 6px 8px 14px rgba(0,0,0,.35);
    font-family: "Red Hat Display", sans-serif; color: var(--white);
  }
  .backdrop-photo {
    position: absolute; left: 0; top: 0; width: 804px; height: 720px;
    background: linear-gradient(180deg, #202225 0%, #2e3136 28%, #3b424b 50%, #2c3036 64%, #111214 84%, #000 100%);
  }
  .fleet-photo {
    position: absolute; left: 104px; top: 226px; width: 632px; height: 190px;
    border-radius: 60px 60px 24px 24px;
    background: linear-gradient(90deg, #6d7480 0%, #7c838e 18%, #c4202c 30%, #d7303a 44%, #8a8f96 56%, #a3a8ae 74%, #6c7178 100%);
    box-shadow: 0 18px 26px rgba(0,0,0,.55);
  }
  .brand { position: absolute; left: 510px; top: 44px; width: 240px; text-align: center; }
  .brand-name { font-weight: 800; font-size: 36px; line-height: 40px; color: var(--brand-blue); letter-spacing: -0.5px; }
  .brand-tagline { font-weight: 900; font-style: italic; font-size: 12px; letter-spacing: 6px; color: var(--tag-grey); margin-top: 2px; }
  .headline { font-family: "Antonio", sans-serif; font-weight: 700; text-transform: uppercase; }
  .headline-top { position: absolute; left: 88px; top: 438px; font-size: 84px; line-height: 1; color: var(--white); letter-spacing: -1px; }
  .headline-main { position: absolute; left: 88px; top: 512px; font-size: 133px; line-height: 1; color: var(--brand-blue); letter-spacing: -2px; }
  .rate-badge {
    position: absolute; left: 555px; top: 467px; width: 180px; height: 180px; border-radius: 50%;
    background: var(--brand-green); text-align: center;
  }
  .rate-label { font-size: 19px; margin-top: 45px; }
  .rate-price { font-family: "Antonio", sans-serif; font-weight: 700; line-height: 1; text-shadow: 2px 3px 4px rgba(0,0,0,.35); }
  .rate-price .currency { font-size: 24px; vertical-align: 30px; }
  .rate-price .amount { font-size: 70px; }
  .rate-price .unit { font-size: 30px; }
  .eligibility { position: absolute; left: 89px; top: 676px; font-size: 15.5px; }
  .offer-title { position: absolute; left: 88px; top: 704px; font-family: "Antonio", sans-serif; font-weight: 700; font-size: 50px; line-height: 1; letter-spacing: -1px; }
  .offer-list { position: absolute; left: 92px; top: 772px; list-style: none; }
  .offer-list li { display: flex; align-items: center; height: 24.5px; font-size: 15.7px; }
  .offer-list svg { width: 26px; height: 26px; margin-right: 5px; }
  .contact-bar { position: absolute; left: 0; top: 950px; width: 804px; height: 57px; }
  .contact-bar svg.bands { position: absolute; left: 0; top: 0; }
  .address, .phone { position: absolute; top: 0; height: 57px; display: flex; align-items: center; }
  .address { left: 48px; }
  .phone { left: 494px; }
  .contact-text { font-size: 14px; line-height: 16px; margin-left: 17px; }
  .phone .contact-text { margin-left: 16px; }
  .phone-tagline { font-weight: 900; font-style: italic; font-size: 14px; letter-spacing: 4.5px; color: var(--tag-dark); }
</style>
</head>
<body>
  <main class="flyer">
    <div class="backdrop-photo" role="img" aria-label="Photo of a modern glass building and paved plaza at dusk"></div>
    <div class="fleet-photo" role="img" aria-label="Photo of a grey SUV, a red compact sedan and a grey full size sedan parked side by side"></div>

    <div class="brand">
      <div class="brand-name">DriveWay</div>
      <div class="brand-tagline">Car &amp; Van Rental</div>
    </div>

    <h1 class="headline">
      <span class="headline-top">Need Car</span>
      <span class="headline-main">Rental?</span>
    </h1>

    <div class="rate-badge">
      <div class="rate-label">Rates as low as</div>
      <div class="rate-price"><span class="currency">$</span><span class="amount">50/</span><span class="unit">DAY</span></div>
    </div>

    <p class="eligibility">We rent cars to holders of a driving license and insurance.</p>

    <h2 class="offer-title">WE OFFER:</h2>
    <ul class="offer-list">
      <li><svg viewBox="0 0 26 26"><path d="M2 15 L9 22 L24 2 L9 17 Z" fill="var(--tick-yellow)"/></svg>Compact cars</li>
      <li><svg viewBox="0 0 26 26"><path d="M2 15 L9 22 L24 2 L9 17 Z" fill="var(--tick-yellow)"/></svg>Mid-size and full size sedans</li>
      <li><svg viewBox="0 0 26 26"><path d="M2 15 L9 22 L24 2 L9 17 Z" fill="var(--tick-yellow)"/></svg>SUV's.</li>
    </ul>

    <footer class="contact-bar">
      <svg class="bands" width="804" height="57" viewBox="0 0 804 57">
        <polygon points="0,0 445,0 432,57 0,57" fill="var(--brand-blue)"/>
        <polygon points="464,0 804,0 804,57 450,57" fill="var(--bar-green)"/>
      </svg>
      <div class="address">
        <svg width="28" height="34" viewBox="0 0 28 34" fill="none" stroke="var(--white)" stroke-width="2.2">
          <path d="M14 32 C5 21 2 16 2 12 A12 12 0 0 1 26 12 C26 16 23 21 14 32 Z"/>
          <circle cx="14" cy="12" r="4.5"/>
        </svg>
        <div class="contact-text">4870 Westfield Avenue<br>Riverton, AL 35090</div>
      </div>
      <div class="phone">
        <svg width="36" height="34" viewBox="0 0 36 34" fill="none" stroke="var(--white)" stroke-width="2.2" stroke-linejoin="round">
          <path d="M4 3 L10 2 L14 10 L10 13 C12 19 16 23 22 25 L25 21 L33 25 L32 31 C20 33 5 21 4 3 Z"/>
        </svg>
        <div class="contact-text">555-014-2280<br><span class="phone-tagline">Car &amp; Van Rental</span></div>
      </div>
    </footer>
  </main>
</body>
</html>
```